依頼詳細
※ワイヤーフレームは以下よりダウンロードしてください
https://15.tomobako-share.example/1227-c93bd7e5a1f0288466d1e7a3b50c9e4a7

※画像素材は以下から使用してください。
https://10.tomobako-share.example/1227-a7e2c9d4b3f81026e5c7a9d0f1b36e58
足りない分はルミナフォトを使用してください

■サイトマップ

1 TOP
2 SHOP INFO
3 MENU
4 CUT
5 COLOR
6 PERM
7 TREATMENT
8 HEAD SPA
9 OTHER
10 ITEM(一覧)
11 ITEM(詳細)
12 GALLERY(一覧)
13 GALLERY(詳細)
14 STAFF(一覧)
15 STAFF(詳細)
16 Q&A(一覧)
17 CONTACT
18 RECRUIT
19 NEWS&BLOG(一覧)
20 NEWS&BLOG(詳細)

■参考サイト(※現行サイト、ポータルサイトなど)
・現行サイト
http://korune-h.example

・参考サイト
https://www.mipotesu.example/

■カラー
└白背景にグレーやベージュなどを入れてうまく高級感を出してください。
└基本的にはサイトのカラーテイストの準拠してください
└背景色には、テクスチャを入れるなどしてうまく高級感を表現してください

■フォントについて
・無料で使えるフォントで作成お願い致します
・OSに紐づくフォントの使用は控えていただければと思います (ヒラギノなど)

■文章について
・可能な限り「ダミーテキスト」を繰り返した文字の配置は避けて頂きたいです
サイトURL
http://korune-h.example
ページ数
1ページ
希望イメージ
シンプル 複雑
単色 カラフル
暗い 明るい
日常 高級
遊び心 厳粛
未来的 伝統的
女性的 男性的
希望する色
黄・オレンジ系、無彩色系
納品ファイル
• イラストレーター形式 (.ai)
• フォトショップ形式 (.psd)
補足説明
◆素材について
Lumina Photo画像をご使用ください。
その際、通常アセットでダウンロード出来る画像のみを使用してください。
Lumina Photo以外の素材を使用する際には、
必ず無料で提供いただける物のみご使用ください。

◆ワイヤーフレームについて
絶対に厳守していただく必要はございません。
デザイン的にこちらの方が良いなどあれば、
そちらを採用してください

◆サイズについて
TOPデザイン自体の画像サイズは、横幅1300pxで提案をお願いできますと幸いです。(縦幅の制限はございません)

※通常業務へ支障が出るため、店舗へのお電話はお控え下さい。

```html
<!DOCTYPE html>
<html lang="ja">
<head>
<meta charset="utf-8">
<title>KORUNE hair salon</title>
<link href="https://fonts.googleapis.com/css2?family=Cormorant+Garamond:wght@400;500;600&family=Noto+Serif+JP:wght@400;500&display=swap" rel="stylesheet">
<style>
:root{
  --white:#ffffff;
  --paper:#f4f3f1;
  --band:#e6e5e3;
  --ink:#3a3a3a;
  --soft:#6f6f6f;
  --line:#c9c7c3;
  --dark:#5b5b5b;
  --btn:#4a4a4a;
  --photo-warm:#c9b49e;
  --photo-skin:#d9bfa8;
  --photo-gray:#b8b4ae;
  --photo-dark:#6a5a4e;
}
*{margin:0;padding:0;box-sizing:border-box}
html,body{width:1200px;height:4940px;overflow:hidden;background:var(--white);color:var(--ink);
  font-family:"Noto Serif JP","Cormorant Garamond",serif}
.page{position:relative;width:1200px;height:4940px}
section,header,footer{position:absolute;left:0;width:1200px}
.abs{position:absolute}
.photo{position:absolute}
.en{font-family:"Cormorant Garamond",serif;letter-spacing:.12em}
.sec-title{position:absolute;left:0;width:1200px;text-align:center}
.sec-title h2{font-family:"Cormorant Garamond",serif;font-weight:500;font-size:30px;letter-spacing:.16em}
.sec-title p{font-size:13px;letter-spacing:.2em;margin-top:6px;color:var(--soft)}
.btn{position:absolute;background:var(--btn);color:var(--white);font-family:"Cormorant Garamond",serif;
  font-size:14px;letter-spacing:.14em;text-align:center;line-height:30px;height:30px}
.body-text{position:absolute;left:0;width:1200px;text-align:center;font-size:13px;line-height:2;color:var(--ink)}

/* header */
.hero{top:0;height:600px;background:linear-gradient(100deg,#d7d3ce 0%,#e4ddd4 40%,#c8ad93 70%,#9c7b62 100%)}
.nav{position:absolute;top:0;left:0;width:1200px;height:52px;background:rgba(255,255,255,.85)}
.nav .brand{position:absolute;left:22px;top:12px;font-family:"Cormorant Garamond",serif;font-size:24px;letter-spacing:.2em;color:var(--ink)}
.nav ul{position:absolute;left:340px;top:0;list-style:none;display:flex;height:52px}
.nav li{font-family:"Cormorant Garamond",serif;font-size:13px;letter-spacing:.1em;width:90px;text-align:center;line-height:52px}
.nav li.contact{background:#8c8c8c;color:var(--white)}
.nav li.reserve{background:#b5b5b5;color:var(--white)}
.nav .menu-icon{position:absolute;right:0;top:0;width:56px;height:52px;background:var(--white)}
.hero .logo{position:absolute;left:330px;top:185px;width:240px;text-align:center;color:var(--white);
  font-family:"Cormorant Garamond",serif;font-size:46px;letter-spacing:.28em}
.hero .tagline{position:absolute;left:20px;top:380px;color:var(--white);font-size:17px;line-height:2;letter-spacing:.12em}

/* news */
.news{top:600px;height:260px}
.news-list{position:absolute;left:358px;top:105px;width:484px;list-style:none}
.news-list li{position:relative;height:36px;border-bottom:1px solid var(--line);font-size:12px;line-height:36px;color:var(--ink)}
.news-list .date{display:inline-block;width:62px;font-family:"Cormorant Garamond",serif}
.news-list .more{position:absolute;right:0;top:7px;width:90px;height:22px;line-height:22px;background:var(--btn);color:var(--white);text-align:center;font-size:11px;font-family:"Cormorant Garamond",serif;letter-spacing:.1em}

/* concept */
.concept{top:865px;height:420px;background:var(--band)}
.concept-card{position:absolute;left:88px;top:0;width:1024px;height:420px;background:linear-gradient(90deg,#efece8,#f8f6f3 60%,#e9e6e2)}
.concept .sec-title{top:40px}

/* menu */
.menu{top:1300px;height:640px}
.menu-grid{position:absolute;left:88px;top:115px;width:1024px}
.tile{position:absolute;height:180px}
.tile span{position:absolute;left:0;right:0;bottom:34px;text-align:center;color:var(--white);font-family:"Cormorant Garamond",serif;font-size:16px;letter-spacing:.16em}

/* blog */
.blog{top:1980px;height:640px;background:var(--band)}
.blog-list{position:absolute;left:240px;top:470px;width:720px;list-style:none}
.blog-list li{height:34px;border-bottom:1px solid var(--line);font-size:12px;line-height:34px}
.blog-list .cat{display:inline-block;width:44px;height:16px;line-height:14px;border:1px solid var(--soft);font-size:10px;text-align:center;margin-right:10px}
.blog-list .date{font-family:"Cormorant Garamond",serif;margin-right:16px}

/* gallery */
.gallery{top:2660px;height:580px}
/* item */
.item{top:3260px;height:660px;background:var(--band)}
/* staff */
.staff{top:3930px;height:400px}
.label{position:absolute;color:var(--white);font-family:"Cormorant Garamond",serif;font-size:15px;letter-spacing:.14em;text-align:center}
/* recruit */
.recruit{top:4340px;height:200px;background:linear-gradient(90deg,#eeeeec,#dcdad6 50%,#f0efed)}
.recruit p{position:absolute;left:740px;top:58px;font-size:12px;line-height:2;color:var(--ink)}
/* footer */
.footer{top:4540px;height:400px;background:var(--dark);color:#e8e8e8}
.footer .brand{position:absolute;left:88px;top:30px;font-family:"Cormorant Garamond",serif;font-size:30px;letter-spacing:.24em}
.footer .address{position:absolute;left:88px;top:130px;font-size:11px;line-height:1.9}
.footer .links{position:absolute;left:552px;top:60px;width:600px;display:grid;grid-template-columns:repeat(5,112px);row-gap:14px;list-style:none}
.footer .links li{font-family:"Cormorant Garamond",serif;font-size:13px;letter-spacing:.1em}
.footer .reserve-btn{position:absolute;left:1030px;top:-38px;width:110px;height:28px;border:1px solid var(--soft);background:var(--white);color:var(--ink);text-align:center;line-height:26px;font-family:"Cormorant Garamond",serif;font-size:12px;letter-spacing:.12em}
.footer .copy{position:absolute;left:0;bottom:14px;width:1200px;text-align:center;font-size:10px;font-family:"Cormorant Garamond",serif;letter-spacing:.1em}
.footer .sns{position:absolute;left:170px;top:42px;width:20px;height:20px;border:1.5px solid #e8e8e8;border-radius:50%}
</style>
</head>
<body>
<div class="page">

<header class="hero">
  <div class="photo" style="left:0;top:0;width:1200px;height:600px;background:linear-gradient(100deg,#d8d4cf 0%,#e6e0d8 42%,#cfb296 68%,#a4846a 100%)" role="img" aria-label="店内で微笑む女性スタイリストの写真"></div>
  <nav class="nav">
    <div class="brand">KORUNE</div>
    <ul>
      <li>TOP</li><li>SHOP INFO</li><li>MENU</li><li>GALLERY</li><li>ITEM</li><li>STAFF</li><li>RECRUIT</li><li class="contact">CONTACT</li><li class="reserve">RESERVE</li>
    </ul>
    <div class="menu-icon">
      <svg width="56" height="52"><g stroke="#3a3a3a" stroke-width="1.5"><line x1="18" y1="19" x2="38" y2="19"/><line x1="18" y1="26" x2="38" y2="26"/><line x1="18" y1="33" x2="38" y2="33"/></g></svg>
    </div>
  </nav>
  <div class="logo">KORUNE</div>
  <p class="tagline">お客様の今までにない<br>「美」を引き出すお手伝いをさせて頂きます</p>
</header>

<section class="news">
  <div class="sec-title" style="top:24px"><h2>NEWS</h2><p>「KORUNEからのお知らせ」</p></div>
  <ul class="news-list">
    <li><span class="date">08.20</span>年末年始の営業日と予約受付のご案内<span class="more">MORE</span></li>
    <li><span class="date">08.14</span>秋の新メニュー導入と営業時間のご案内<span class="more">MORE</span></li>
  </ul>
</section>

<section class="concept">
  <div class="concept-card"></div>
  <div class="photo" style="left:250px;top:150px;width:150px;height:200px;background:linear-gradient(160deg,#c99f7c,#e7dbcc)" role="img" aria-label="花を持つ女性の写真"></div>
  <div class="sec-title"><h2>CONCEPT</h2><p>「新たな自分を見つける」</p></div>
  <p class="body-text" style="top:150px;font-size:12px">経験豊かなスタイリストが一人ひとりに寄り添い<br>その方だけの似合うスタイルをご提案します<br>ゆったりとした空間で<br>髪と心を休めるひとときをお過ごしください<br>新しい自分に出会う場所<br>それがKORUNEです</p>
  <div class="btn" style="left:540px;top:340px;width:120px">MORE</div>
</section>

<section class="menu">
  <div class="sec-title" style="top:40px"><h2>MENU</h2><p>「貴方のなりたいをサポートする豊富なメニュー」</p></div>
  <div class="menu-grid">
    <div class="tile" style="left:0;top:0;width:300px;background:linear-gradient(120deg,#7a6558,#c9ad95)" role="img" aria-label="カット施術の写真"><span>CUT</span></div>
    <div class="tile" style="left:352px;top:0;width:320px;background:linear-gradient(120deg,#5e4a3e,#d2b49a)" role="img" aria-label="カラー施術の写真"><span>COLOR</span></div>
    <div class="tile" style="left:704px;top:0;width:320px;background:linear-gradient(120deg,#8c8a86,#d6d2cb)" role="img" aria-label="パーマ施術の写真"><span>PERM</span></div>
    <div class="tile" style="left:0;top:210px;width:300px;background:linear-gradient(120deg,#a59a8f,#e4ddd4)" role="img" aria-label="トリートメント施術の写真"><span>TREATMENT</span></div>
    <div class="tile" style="left:352px;top:210px;width:320px;background:linear-gradient(120deg,#9d8a79,#e2d4c4)" role="img" aria-label="ヘッドスパの写真"><span>HEAD SPA</span></div>
    <div class="tile" style="left:704px;top:210px;width:320px;background:linear-gradient(120deg,#8f9279,#d9d5c6)" role="img" aria-label="その他メニューのイメージ写真"><span>OTHER</span></div>
  </div>
</section>

<section class="blog">
  <div class="sec-title" style="top:40px"><h2>BLOG</h2><p>「最新の髪の毛の情報やKORUNEの日常を情報発信しております」</p></div>
  <div class="photo" style="left:88px;top:135px;width:630px;height:300px;background:linear-gradient(180deg,#e9e7e2,#b6a896 60%,#8d7c69)" role="img" aria-label="サロン外観の写真"></div>
  <div class="photo" style="left:735px;top:135px;width:377px;height:145px;background:linear-gradient(120deg,#d9d6d1,#f2f1ee)" role="img" aria-label="明るい店内のセット面の写真"></div>
  <div class="photo" style="left:735px;top:290px;width:377px;height:145px;background:linear-gradient(120deg,#6f6a63,#d3cfc8)" role="img" aria-label="シャンプー台のある店内の写真"></div>
  <ul class="blog-list">
    <li><span class="cat">NEWS</span><span class="date">2021/10/30</span>秋冬おすすめのヘアカラーと季節のケア方法のご紹介</li>
    <li><span class="cat">STAFF</span><span class="date">2021/10/28</span>新しいスタッフが仲間に加わりました、ご来店お待ちしております</li>
  </ul>
  <div class="btn" style="left:520px;top:560px;width:160px">BLOG 一覧を見る</div>
</section>

<section class="gallery">
  <div class="sec-title" style="top:40px"><h2>GALLERY</h2><p>「あなただけのスタイルを叶えます」</p></div>
  <div class="photo" style="left:0;top:105px;width:350px;height:230px;background:linear-gradient(130deg,#b5552c,#e3b38d 60%,#f0e6da)" role="img" aria-label="オレンジ系ショートヘアのスタイル写真"></div>
  <div class="photo" style="left:395px;top:105px;width:410px;height:230px;background:linear-gradient(120deg,#efeae4,#4a3a30 45%,#2d231d 60%,#e8e1d9)" role="img" aria-label="艶のあるストレートロングのスタイル写真"></div>
  <div class="photo" style="left:830px;top:105px;width:370px;height:230px;background:linear-gradient(120deg,#8e6f5a,#c35a6a 45%,#e7c9a8)" role="img" aria-label="花束を持つ女性のスタイル写真"></div>
  <p class="body-text" style="top:385px;font-size:12px">一人ひとりの骨格や髪質に合わせたスタイルを<br>季節ごとのトレンドを取り入れながらご提案しています<br>お客様のご来店時の参考にご覧ください</p>
  <div class="btn" style="left:500px;top:468px;width:200px">GALLERY 一覧を見る</div>
</section>

<section class="item">
  <div class="sec-title" style="top:40px"><h2>ITEM</h2><p>「あなたの美を引き出す商品やアイテムを販売しております」</p></div>
  <div class="photo" style="left:0;top:150px;width:380px;height:230px;background:linear-gradient(120deg,#5a3d24,#c98a3e 50%,#e8c48e)" role="img" aria-label="ヘアオイルのボトルの写真"></div>
  <div class="photo" style="left:395px;top:150px;width:405px;height:230px;background:linear-gradient(120deg,#b9b2a6,#f3f1ed 55%,#d8d2c8)" role="img" aria-label="白いクリームとチューブの写真"></div>
  <div class="photo" style="left:820px;top:150px;width:380px;height:230px;background:linear-gradient(120deg,#e9e4dc,#3e4660 55%,#a99a88)" role="img" aria-label="シャンプーボトルの写真"></div>
  <p class="body-text" style="top:420px;font-size:12px">サロンで使用している商品をご自宅でもお使いいただけます<br>スタッフが髪質に合わせて最適なアイテムをご案内します<br>お気軽にご相談ください</p>
  <div class="btn" style="left:510px;top:535px;width:180px">ITEM 一覧を見る</div>
</section>

<section class="staff">
  <div class="photo" style="left:88px;top:60px;width:282px;height:300px;background:linear-gradient(120deg,#6b5a50,#b7a599 50%,#3f3c4e)" role="img" aria-label="スタッフの写真"></div>
  <div class="label" style="left:180px;top:196px;width:100px">RESERVE<br><span style="font-size:12px">ご予約</span></div>
  <div class="photo" style="left:380px;top:60px;width:732px;height:145px;background:linear-gradient(120deg,#8a7f77,#c8c2bb 50%,#6a625c)" role="img" aria-label="ハサミやブラシなどの道具の写真"></div>
  <div class="photo" style="left:380px;top:215px;width:350px;height:145px;background:linear-gradient(120deg,#9c8d83,#d8d0c7)" role="img" aria-label="施術中のスタッフの写真"></div>
  <div class="label" style="left:505px;top:315px;width:100px">STAFF</div>
  <div class="photo" style="left:740px;top:215px;width:372px;height:145px;background:linear-gradient(120deg,#d6d2cc,#f0eeeb)" role="img" aria-label="ロッドが並ぶ施術の写真"></div>
  <div class="label" style="left:876px;top:300px;width:100px">RECRUIT<br><span style="font-size:12px">求人</span></div>
</section>

<section class="recruit">
  <div class="photo" style="left:0;top:0;width:700px;height:200px;background:linear-gradient(90deg,#d9d7d3,#eeedea)" role="img" aria-label="白い椅子が並ぶ明るい店内の写真"></div>
  <p>KORUNEでは一緒に働く仲間を募集しています<br>経験や年齢は問いません、まずはご連絡ください<br>「あなたの美しさを一緒に届けませんか」</p>
</section>

<footer class="footer">
  <div class="reserve-btn">RESERVE</div>
  <div class="brand">KORUNE</div>
  <div class="sns"></div>
  <p class="address">KORUNE hair<br>〒556-0031 大阪府港央市緑見町2丁目8-14<br>コルネビル1F<br>TEL 06-4578-2216<br>営業時間 10:00〜20:00（日祝 10:00〜19:00）<br>定休日 毎週火曜日</p>
  <ul class="links">
    <li>TOP</li><li>SHOP INFO</li><li>ITEM</li><li>GALLERY</li><li>STAFF</li>
    <li>MENU</li><li>COLOR</li><li>PERM</li><li>TREATMENT</li><li>RECRUIT</li>
    <li>CUT</li><li>HEAD SPA</li><li>OTHER</li><li>NEWS</li><li>BLOG</li>
    <li>CONTACT</li><li>Q&amp;A</li>
  </ul>
  <p class="copy">© KORUNE All Rights Reserved.</p>
</footer>

</div>
</body>
</html>
```